Business Cards

The name of our firm is "Tallpine Insurance adjusters"
We separate ourselves from all other public adjusters because most of us worked for the insurance companies so we understand their games.
As Insurance adjusters we represent the Insured, not the insurance companies. Our # 1 priority is to handle the entire claim process as seamless as possible on behalf of the homeowner/business owner so they don't have to deal with the hassles and headaches. Just as the logo your team designed, I want the cards to stand out from everyone elses. I also want the cards to help better understand our services and Value on hiring us and value that we can offer.
I uploaded the logo whenever I created the project. I don't see an option on re uploading the logo anywhere. Any advise??

```html
<!DOCTYPE html>
<html lang="en">
<head>
<meta charset="utf-8">
<title>Tallpine Insurance Adjusters – Business Cards</title>
<link rel="stylesheet" href="https://fonts.googleapis.com/css2?family=Josefin+Sans:wght@400;600;700&display=swap">
<style>
  :root {
    --backdrop: #c3c5c7;
    --front-bg: #03090d;
    --front-glow: #0a1820;
    --back-bg: #ffffff;
    --brand-blue: #1a6fa3;
    --band-top: #0f72ad;
    --band-bottom: #0b4f7e;
    --band-edge: #0a2333;
    --on-band: #ffffff;
  }
  * { margin: 0; padding: 0; box-sizing: border-box; }
  html, body {
    width: 1187px;
    height: 1200px;
    overflow: hidden;
    background: var(--backdrop);
    font-family: "Josefin Sans", sans-serif;
  }
  .stage {
    position: relative;
    width: 1187px;
    height: 1200px;
  }
  .card {
    position: absolute;
    left: 214px;
    width: 760px;
    height: 436px;
  }
  .card--front {
    top: 119px;
    background: radial-gradient(ellipse at 50% 65%, var(--front-glow) 0%, var(--front-bg) 60%);
  }
  .card--back {
    top: 641px;
    background: var(--back-bg);
  }
  .brand-mark {
    position: absolute;
    left: 0;
    right: 0;
    text-align: center;
    color: var(--brand-blue);
    font-weight: 700;
    text-transform: uppercase;
    line-height: 1.05;
  }
  .brand-mark__name { display: block; font-size: 40px; letter-spacing: 1px; }
  .brand-mark__line { display: block; font-size: 13px; letter-spacing: 1.5px; }
  .card--front .brand-mark { top: 176px; }
  .card--back .brand-mark { top: 138px; }
  .contact-band {
    position: absolute;
    left: 0;
    right: 0;
    top: 302px;
    height: 92px;
    background: linear-gradient(180deg, var(--band-top), var(--band-bottom));
    border-top: 2px solid var(--band-edge);
    border-bottom: 2px solid var(--band-edge);
    color: var(--on-band);
  }
  .contact-band__name {
    position: absolute;
    left: 72px;
    top: 31px;
    font-size: 31px;
    font-weight: 600;
    letter-spacing: 1.5px;
    text-transform: uppercase;
  }
  .contact-list {
    position: absolute;
    left: 412px;
    top: 18px;
    list-style: none;
    font-size: 19px;
    letter-spacing: 2px;
  }
  .contact-list li {
    display: flex;
    align-items: center;
    height: 32px;
  }
  .contact-list svg {
    width: 14px;
    height: 14px;
    margin-right: 11px;
    fill: var(--on-band);
  }
</style>
</head>
<body>
<main class="stage">
  <section class="card card--front" aria-label="Card front">
    <div class="brand-mark">
      <span class="brand-mark__name">Tallpine</span>
      <span class="brand-mark__line">Insurance Adjusters</span>
    </div>
  </section>

  <section class="card card--back" aria-label="Card back">
    <div class="brand-mark">
      <span class="brand-mark__name">Tallpine</span>
      <span class="brand-mark__line">Insurance Adjusters</span>
    </div>
    <div class="contact-band">
      <p class="contact-band__name">Marcus Hadley</p>
      <ul class="contact-list">
        <li>
          <svg viewBox="0 0 24 24" aria-hidden="true"><path d="M6.6 10.8a15.1 15.1 0 0 0 6.6 6.6l2.2-2.2c.3-.3.7-.4 1-.2 1.1.4 2.3.6 3.6.6.6 0 1 .4 1 1V20c0 .6-.4 1-1 1A17 17 0 0 1 3 4c0-.6.4-1 1-1h3.5c.6 0 1 .4 1 1 0 1.3.2 2.5.6 3.6.1.3 0 .7-.2 1z"/></svg>
          555-014-2276
        </li>
        <li>
          <svg viewBox="0 0 24 24" aria-hidden="true"><path d="M2 5h20v2l-10 6L2 7z"/><path d="M2 9l10 6 10-6v10H2z"/></svg>
          hello@tallpineclaims.com
        </li>
      </ul>
    </div>
  </section>
</main>
</body>
</html>
```